Web Design Accounting-Tax and related business service online.

We are looking to develop a website/online application for users in the South African market to register and buy Accounting/tax and related services online. (New business registrations/Income tax returns/Payroll) etc

The Domain will be www.ledgerbright-hub.co.za and the business will be run under Valkmere Financial Services.

The domain - www.ledgerbright-hub.co.za will be used as the "trading" name of the site, so any sections that possible make use name use domain name.

We are looking for designs for the website.

Here is the requirements as from the developer

• Home Page: Design of the home page of the website.
• Forms: We have different forms in the application. Need any one form designed. Just look and feel without functionality.
• Member Area: when a user will log in, the layout of dashboard to show them.

UPDATE (Previously HTML required) - Can be in PSD format for this Contest.

(If you prepared/capable to handle the PSD to HTML conversation you can quote seperate for this)

Websites that offer similar services (Not for design inspiration please, but idea of possible website layout etc)

http://www.quillpenny-direct.co.za/
http://www.venturefile-desk.co.za/

See our current static website for colour schemes that I like.

www.valkmere.co.za

Prefer clean, modern - uncluttered look.

Target Market(s)

Users that pefer employing tech and ease of obtaining services online to having Accountant physically close.

Industry/Entity Type

Business Service

Requirements
Must have
• Clean, Modern, uncluttered look.

Nice to have

Should not have
• Old "boring" stiff accounting designs. No clutter or too busy.

```html
<!DOCTYPE html>
<html lang="en">
<head>
<meta charset="utf-8">
<title>Valkmere Financial Services</title>
<link href="https://fonts.googleapis.com/css2?family=Open+Sans:wght@400;600;700&family=Oswald:wght@700&display=swap" rel="stylesheet">
<style>
:root{
  --orange:#f7891c;
  --orange-light:#fba94a;
  --orange-deep:#e86a06;
  --brown:#6a2d00;
  --text:#333;
  --muted:#777;
  --line:#d8d8d8;
  --link:#2a6bb5;
  --photo-dark:#2f5a7a;
  --photo-light:#c9dbe8;
}
*{box-sizing:border-box;margin:0;padding:0}
html,body{width:782px;height:1200px;overflow:hidden;background:#fff}
body{position:relative;font-family:"Open Sans",sans-serif;color:var(--text)}
.abs{position:absolute}
.brand-name{left:188px;top:50px;font-size:46px;font-weight:700;color:#333;letter-spacing:1px;line-height:1}
.brand-sub{left:189px;top:102px;font-size:17px;letter-spacing:4px;color:#222;white-space:nowrap}
.brand-reg{left:189px;top:123px;font-size:9px;color:var(--link)}
.account-bar{right:33px;top:14px;font-size:9px;color:#333}
.social{right:30px;top:52px;display:flex;align-items:center;gap:4px;font-size:9px;color:var(--muted)}
.social span.dot{width:25px;height:25px;border-radius:50%;background:#7a9cc6;display:inline-block}
.social span.dot:nth-child(3){background:#a5d0e6}
.social span.dot:nth-child(5){background:#a9b8d8}
.social span.dot:nth-child(6){background:var(--orange)}
.social .label{margin-right:6px}
.search{left:552px;top:107px;width:197px;height:31px;border:1px solid var(--line);border-radius:6px;padding:4px 8px}
.search div{border:1px solid var(--line);height:20px;width:170px;font-size:11px;color:#999;padding:1px 8px}
.search svg{position:absolute;right:10px;top:-8px}
.nav{left:215px;top:151px;width:537px;height:23px;border-top:1px solid var(--line);border-bottom:1px solid var(--line);display:flex;justify-content:flex-end;align-items:center;gap:14px;font-size:10.5px;font-weight:600;color:#666;padding-right:7px}
.nav i{font-style:normal;color:#999}
.hero{left:30px;top:194px;width:537px;height:184px;border-radius:4px;background:linear-gradient(135deg,var(--photo-light),#7fa3c0 50%,var(--photo-dark))}
.signup{left:583px;top:194px;width:169px}
.signup h2{font-size:13.5px;font-weight:400;color:#444;margin:0 0 12px;white-space:nowrap;line-height:20px}
.field{height:23px;border:1px solid #bbb;border-radius:4px;margin-bottom:6px;font-size:9px;color:#aaa;padding:4px 10px}
.agree{font-size:9px;margin-top:14px;display:flex;align-items:center;gap:5px;white-space:nowrap}
.agree a{color:var(--link);text-decoration:none}
.cta{margin-top:11px;width:146px;height:30px;border-radius:4px;background:linear-gradient(var(--orange-light),var(--orange-deep));color:#fff;font-weight:700;font-size:12px;text-align:center;line-height:28px;border:1px solid #d86a10}
.service{top:401px;width:231px;height:92px;border:1px solid var(--line);border-radius:4px}
.service .icon{position:absolute;left:7px;top:16px;width:56px;height:56px;border-radius:50%;background:linear-gradient(135deg,#9cc6e8,#3f7fc0)}
.service h3{position:absolute;left:68px;top:10px;font-size:11.5px;font-weight:400}
.service p{position:absolute;left:68px;top:32px;font-size:7px;line-height:9px;width:150px}
.service .row{position:absolute;left:68px;top:57px;display:flex;align-items:center;gap:4px;font-size:7px;font-weight:700}
.service .row b{display:inline-block;width:84px;height:17px;border:1px solid #ccc;background:#f3f3f3}
.service .go{width:21px;height:21px;border-radius:50%;background:#d4361a;border:2px solid #f3a07a;color:#fff;font-size:8px;line-height:17px;text-align:center;margin-left:8px}
.banner{left:30px;top:516px;width:721px;height:184px;border-radius:6px;overflow:hidden;background:radial-gradient(circle at 15% 40%,#f08a2e,transparent 40%),radial-gradient(circle at 90% 80%,#e8781a,transparent 35%),linear-gradient(#ff9a3a,#f47e16);font-family:"Oswald",sans-serif;font-weight:700}
.banner span{position:absolute;line-height:1;white-space:nowrap}
.b-your{left:224px;top:20px;font-size:50px;color:#fff}
.b-mid{left:129px;top:72px;font-size:43px;color:var(--brown);transform:scaleX(1.16);transform-origin:left top}
.b-partner{left:303px;top:114px;font-size:58px;color:#3a1a00}
.footer{left:30px;top:726px;width:722px;height:459px;border-radius:6px;overflow:hidden;background:radial-gradient(circle at 120% 100%,#fb7c0c 45%,transparent 45.3%),radial-gradient(ellipse 140% 120% at 110% 50%,#fb8a1e 55%,transparent 55.3%),#fc9a3a}
.links{position:absolute;left:118px;top:36px;display:grid;grid-template-columns:repeat(4,140px);row-gap:22px;color:#fff}
.links h4{font-size:15.5px;font-weight:700;margin-bottom:8px;letter-spacing:.5px;color:#fff3e6}
.links li{list-style:none;font-size:12px;letter-spacing:.6px;line-height:21.6px}
</style>
</head>
<body>
<div class="abs brand-name">Valkmere</div>
<div class="abs brand-sub">Financial Services CC</div>
<div class="abs brand-reg">CK 2011/204817/23</div>
<div class="abs account-bar">You are not logged in &nbsp;|&nbsp; Login or Register</div>
<div class="abs social"><span class="label">Follow us</span><span class="dot"></span><span class="dot"></span><span class="dot"></span><span class="dot"></span><span class="dot"></span></div>
<div class="abs search"><div>Search our site</div>
<svg width="52" height="42" viewBox="0 0 52 42"><circle cx="18" cy="14" r="12" fill="#dbe9f5" stroke="#8aa" stroke-width="3"/><line x1="27" y1="22" x2="48" y2="38" stroke="#555" stroke-width="5" stroke-linecap="round"/></svg></div>
<nav class="abs nav"><span>Home</span><i>|</i><span>Package Services</span><i>|</i><span>Individual Services</span><i>|</i><span>Contact Us</span></nav>
<div class="abs hero" role="img" aria-label="Photo of glasses, calculator and pen on a financial spreadsheet"></div>
<form class="abs signup">
<h2>Ut enim ad minim veniam</h2>
<div class="field">Email</div><div class="field">Password</div><div class="field">Confirm password</div>
<div class="agree"><svg width="11" height="11" viewBox="0 0 11 11"><circle cx="5.5" cy="5.5" r="4.8" fill="#fff" stroke="#2a6bb5"/><path d="M3 5.6l1.8 1.8L8 4" fill="none" stroke="#2a6bb5" stroke-width="1.4"/></svg>I agree to the <a>Terms of Service</a></div>
<div class="cta">Duis aute irure dolor</div>
</form>
<div class="abs service" style="left:31px"><div class="icon" role="img" aria-label="Compass illustration"></div><h3>Lorem ipsum dolor</h3><p>Ut enim ad minim veniam, quis nostrud exercitation ullamco laboris</p><div class="row">Duis aute <b></b><span class="go">GO</span></div></div>
<div class="abs service" style="left:277px"><div class="icon" role="img" aria-label="Illustration of two users" style="background:linear-gradient(135deg,#f4c9a0,#8bbf5a)"></div><h3>Lorem ipsum dolor</h3><p>Ut enim ad minim veniam, quis nostrud exercitation ullamco laboris</p><div class="row">Duis aute <b></b><span class="go">GO</span></div></div>
<div class="abs service" style="left:522px"><div class="icon" role="img" aria-label="Illustration of office buildings" style="background:linear-gradient(135deg,#6fbf4a,#3c6fd0)"></div><h3>Lorem ipsum dolor</h3><p>Ut enim ad minim veniam, quis nostrud exercitation ullamco laboris</p><div class="row">Duis aute <b></b><span class="go">GO</span></div></div>
<div class="abs banner" role="img" aria-label="Orange banner with scattered numbers: your Accounting-Bookkeeping-Tax partner"><span class="b-your">your</span><span class="b-mid">Accounting-Bookkeeping-Tax</span><span class="b-partner">partner</span></div>
<footer class="abs footer"><div class="links">
<div><h4>Lorem</h4><ul><li>Ut enim</li><li>Ad minim</li><li>Veniam</li><li>Quis nostrud</li></ul></div>
<div><h4>Lorem</h4><ul><li>Ut enim</li><li>Ad minim</li><li>Veniam</li><li>Quis nostrud</li></ul></div>
<div><h4>Lorem</h4><ul><li>Ut enim</li><li>Ad minim</li><li>Veniam</li><li>Quis nostrud</li></ul></div>
<div><h4>Lorem</h4><ul><li>Ut enim</li><li>Ad minim</li><li>Veniam</li><li>Quis nostrud</li></ul></div>
<div><h4>Lorem</h4><ul><li>Ut enim</li><li>Ad minim</li><li>Veniam</li><li>Quis nostrud</li></ul></div>
<div><h4>Lorem</h4><ul><li>Ut enim</li><li>Ad minim</li><li>Veniam</li><li>Quis nostrud</li></ul></div>
<div><h4>Lorem</h4><ul><li>Ut enim</li><li>Ad minim</li><li>Veniam</li><li>Quis nostrud</li></ul></div>
<div><h4>Lorem</h4><ul><li>Ut enim</li><li>Ad minim</li><li>Veniam</li><li>Quis nostrud</li></ul></div>
<div><h4>Lorem</h4><ul><li>Ut enim</li><li>Ad minim</li><li>Veniam</li><li>Quis nostrud</li></ul></div>
<div><h4>Lorem</h4><ul><li>Ut enim</li><li>Ad minim</li><li>Veniam</li><li>Quis nostrud</li></ul></div>
<div><h4>Lorem</h4><ul><li>Ut enim</li><li>Ad minim</li><li>Veniam</li><li>Quis nostrud</li></ul></div>
<div><h4>Lorem</h4><ul><li>Ut enim</li><li>Ad minim</li><li>Veniam</li><li>Quis nostrud</li></ul></div>
</div></footer>
</body>
</html>
```